An our door sign really promoting our clinic and services

We have a new sports medicine clinic called HALLCREST SPORTS MEDICINE.
We want to make a really nice external sign at our clinic using a photo of our team we really like. I have attached the photo.
We want to simply include our LOGO and also signs with these slogan options. So we want different signs with these different slogans so we can choose what we really like.
This should be a simple and quite design.

The SLOGANS WE WOULD LIKE TO SEE ON THE SIGN (only one slogan per sign in the drafts)

1. Your Journey. Our Expertise
2. Where better health begins
3. Building the best version of you
4. Your health, in expert hands
5. Reaching new heights in your health
6. Your path to peak performance starts here

I have also included different versions of our logo based on the background and how you set the sign up

So summary
1. Image attached
2. Slogan options we would like to see them all
3. Logo attached (various options based on how you set the background up)
4. Size of sign is 2935mm wide x 1885mm high

```html
<!DOCTYPE html>
<html lang="en">
<head>
<meta charset="utf-8">
<title>Hallcrest Sports Medicine – Exterior Sign Options</title>
<link href="https://fonts.googleapis.com/css2?family=Exo+2:ital,wght@0,700;0,800;1,800&display=swap" rel="stylesheet">
<style>
  :root {
    --bg: #e4e5e7;
    --cyan: #4cc3e6;
    --navy: #141c4a;
    --white: #ffffff;
    --photo-dark: #1e2538;
    --photo-mid: #4a4a52;
    --photo-wood: #8a6a52;
    --photo-light: #d6d9df;
  }
  * { box-sizing: border-box; margin: 0; padding: 0; }
  html, body {
    width: 1200px;
    height: 600px;
    overflow: hidden;
    background: var(--bg);
    font-family: "Exo 2", sans-serif;
  }
  .sign-sheet {
    position: absolute;
    left: 27px;
    top: 54px;
    display: grid;
    grid-template-columns: repeat(3, 374px);
    grid-template-rows: repeat(2, 239px);
    column-gap: 14px;
    row-gap: 13px;
  }
  .sign {
    position: relative;
    background: var(--cyan);
    box-shadow: 0 4px 8px rgba(0, 0, 0, 0.18);
    overflow: hidden;
  }
  .sign__photo {
    position: absolute;
    left: 0;
    right: 0;
    top: 6px;
    height: 163px;
    border-top-left-radius: 30px;
    background:
      linear-gradient(90deg, rgba(138,106,82,0.9) 0%, rgba(30,37,56,0.95) 22%, var(--photo-dark) 40%, #263056 62%, rgba(200,204,212,0.95) 82%, var(--photo-light) 100%);
  }
  .sign__panel {
    position: absolute;
    left: 0;
    right: 0;
    top: 169px;
    height: 65px;
    background: var(--white);
    border-bottom-right-radius: 30px;
    display: flex;
    flex-direction: column;
    align-items: center;
    justify-content: flex-start;
    padding-top: 6px;
  }
  .brand {
    display: flex;
    align-items: center;
    gap: 10px;
    color: var(--navy);
    font-weight: 800;
  }
  .brand__dot {
    width: 30px;
    height: 30px;
    border-radius: 50%;
    background: var(--cyan);
  }
  .brand__name {
    display: flex;
    flex-direction: column;
    line-height: 1;
  }
  .brand__main {
    font-size: 22px;
    letter-spacing: 0.5px;
  }
  .brand__sub {
    font-size: 9px;
    letter-spacing: 4.6px;
    margin-top: 2px;
  }
  .slogan {
    margin-top: 6px;
    color: var(--navy);
    font-weight: 800;
    font-style: italic;
    font-size: 13px;
    letter-spacing: 0.3px;
    white-space: nowrap;
  }
  .slogan--medium { font-size: 11.5px; }
  .slogan--long { font-size: 10px; }
</style>
</head>
<body>
  <main class="sign-sheet">
    <article class="sign">
      <div class="sign__photo" role="img" aria-label="Team photo: clinician showing a tablet to a patient in the clinic gym"></div>
      <div class="sign__panel">
        <div class="brand"><span class="brand__dot"></span><span class="brand__name"><span class="brand__main">HALLCREST</span><span class="brand__sub">SPORTS MEDICINE</span></span></div>
        <p class="slogan">Your Journey Our Expertise</p>
      </div>
    </article>
    <article class="sign">
      <div class="sign__photo" role="img" aria-label="Team photo: clinician showing a tablet to a patient in the clinic gym"></div>
      <div class="sign__panel">
        <div class="brand"><span class="brand__dot"></span><span class="brand__name"><span class="brand__main">HALLCREST</span><span class="brand__sub">SPORTS MEDICINE</span></span></div>
        <p class="slogan">Where Better Health Begins</p>
      </div>
    </article>
    <article class="sign">
      <div class="sign__photo" role="img" aria-label="Team photo: clinician showing a tablet to a patient in the clinic gym"></div>
      <div class="sign__panel">
        <div class="brand"><span class="brand__dot"></span><span class="brand__name"><span class="brand__main">HALLCREST</span><span class="brand__sub">SPORTS MEDICINE</span></span></div>
        <p class="slogan slogan--medium">Building the Best Version of You</p>
      </div>
    </article>
    <article class="sign">
      <div class="sign__photo" role="img" aria-label="Team photo: clinician showing a tablet to a patient in the clinic gym"></div>
      <div class="sign__panel">
        <div class="brand"><span class="brand__dot"></span><span class="brand__name"><span class="brand__main">HALLCREST</span><span class="brand__sub">SPORTS MEDICINE</span></span></div>
        <p class="slogan">Your Health in Expert Hands</p>
      </div>
    </article>
    <article class="sign">
      <div class="sign__photo" role="img" aria-label="Team photo: clinician showing a tablet to a patient in the clinic gym"></div>
      <div class="sign__panel">
        <div class="brand"><span class="brand__dot"></span><span class="brand__name"><span class="brand__main">HALLCREST</span><span class="brand__sub">SPORTS MEDICINE</span></span></div>
        <p class="slogan slogan--long">Reaching New Heights in Your Health</p>
      </div>
    </article>
    <article class="sign">
      <div class="sign__photo" role="img" aria-label="Team photo: clinician showing a tablet to a patient in the clinic gym"></div>
      <div class="sign__panel">
        <div class="brand"><span class="brand__dot"></span><span class="brand__name"><span class="brand__main">HALLCREST</span><span class="brand__sub">SPORTS MEDICINE</span></span></div>
        <p class="slogan slogan--long">Your Path to Peak Performance Starts Here</p>
      </div>
    </article>
  </main>
</body>
</html>
```